Book Cover "Venice"

Creation of a cover (14 x 20.5 cm + bleed area) for a book:
Image: “BrumeVerte” (Tiff joined)
AUTHOR: Corinne Valmer
TITLE: The murmurs of Lorient
PUBLISHER: Editions Pluvane (AT THE BOTTOM OF THE COVER)

Target Market(s)

Readers of romantic novels

Industry/Entity Type

Book

```html
<!DOCTYPE html>
<html lang="fr">
<head>
<meta charset="utf-8">
<title>Les Murmures de Lorient — Corinne Valmer</title>
<link rel="stylesheet" href="https://fonts.googleapis.com/css2?family=Cinzel:wght@400;500&family=Montserrat:wght@700&display=swap">
<style>
  :root {
    --page-bg: #e7e7e7;
    --sky-top: #3a0f1f;
    --sky-upper: #8c1522;
    --sky-mid: #d22324;
    --sky-glow: #ff4a1c;
    --sky-low: #e0341c;
    --sky-haze: #b8261f;
    --city-dark: #160a0e;
    --city-deep: #0f070a;
    --title-gold: #ffe07a;
    --text-cream: #fbf3ea;
    --rule-white: #f6ece4;
  }
  * { margin: 0; padding: 0; box-sizing: border-box; }
  html, body {
    width: 1200px;
    height: 1200px;
    overflow: hidden;
    background: var(--page-bg);
  }
  .book-cover {
    position: absolute;
    left: 233px;
    top: 51px;
    width: 734px;
    height: 1098px;
    overflow: hidden;
  }
  .cover-image {
    position: absolute;
    inset: 0;
    background:
      linear-gradient(180deg,
        rgba(22,10,14,0) 0%,
        rgba(22,10,14,0) 66%,
        rgba(22,10,14,0.55) 74%,
        rgba(22,10,14,0.88) 82%,
        var(--city-dark) 90%,
        var(--city-deep) 100%),
      radial-gradient(ellipse 70% 14% at 40% 40%, rgba(70,20,40,0.35) 0%, rgba(70,20,40,0) 100%),
      radial-gradient(ellipse 60% 10% at 20% 57%, rgba(60,20,35,0.3) 0%, rgba(60,20,35,0) 100%),
      radial-gradient(ellipse 80% 22% at 55% 62%, rgba(255,90,30,0.55) 0%, rgba(255,90,30,0) 100%),
      radial-gradient(ellipse 50% 30% at 100% 0%, rgba(40,12,24,0.6) 0%, rgba(40,12,24,0) 100%),
      linear-gradient(180deg,
        var(--sky-top) 0%,
        var(--sky-upper) 10%,
        var(--sky-mid) 24%,
        var(--sky-haze) 38%,
        var(--sky-mid) 48%,
        var(--sky-low) 56%,
        var(--sky-glow) 63%,
        var(--sky-low) 72%,
        var(--sky-mid) 80%,
        var(--sky-upper) 100%);
  }
  .cover-type {
    position: absolute;
    inset: 0;
    width: 734px;
    height: 1098px;
  }
  .author-name {
    font-family: "Cinzel", serif;
    font-size: 38px;
    fill: var(--text-cream);
  }
  .title-small {
    font-family: "Cinzel", serif;
    font-size: 40px;
    fill: var(--text-cream);
  }
  .title-main {
    font-family: "Cinzel", serif;
    fill: var(--title-gold);
  }
  .title-rule {
    stroke: var(--rule-white);
    stroke-width: 2;
  }
  .publisher-line {
    font-family: "Montserrat", sans-serif;
    font-weight: 700;
    font-size: 16.5px;
    fill: #ffffff;
  }
</style>
</head>
<body>
  <main class="book-cover">
    <div class="cover-image" role="img" aria-label="Photograph BrumeVerte: blazing red sunset sky over a silhouetted domed church and glowing street lanterns"></div>
    <svg class="cover-type" viewBox="0 0 734 1098" xmlns="http://www.w3.org/2000/svg">
      <text class="author-name" x="367" y="76" text-anchor="middle" textLength="448" lengthAdjust="spacing">CORINNE VALMER</text>

      <line class="title-rule" x1="47" y1="176" x2="302" y2="176"/>
      <line class="title-rule" x1="433" y1="176" x2="690" y2="176"/>
      <text class="title-small" x="367" y="193" text-anchor="middle">LES</text>

      <text class="title-main" x="49" y="325" font-size="148" textLength="640" lengthAdjust="spacingAndGlyphs">MURMURES</text>

      <line class="title-rule" x1="47" y1="367" x2="302" y2="367"/>
      <line class="title-rule" x1="433" y1="367" x2="690" y2="367"/>
      <text class="title-small" x="367" y="383" text-anchor="middle">DE</text>

      <text class="title-main" x="42" y="553" font-size="190" textLength="646" lengthAdjust="spacingAndGlyphs">LORIENT</text>

      <text class="publisher-line" x="367" y="1072" text-anchor="middle">PUBLISHER: EDITIONS PLUVANE</text>
    </svg>
  </main>
</body>
</html>
```